Item Change Management Brochure / FAQ

Create a very stunning, infographic based brochure around a process Birchline Supply Company calls "Item Change Management". The audience for the brochure are Birchline Supply retail store owners and operators who need to be amazed by the program. This brochure is to make it easy for Birchline Supply store owners to understand the program, its benefits, and the process behind it. Here are some important notes about the brochure:

* Must all fit content on 2 pages - a front and back side - 8-1/2x11"
* Font must be no smaller than size 11 Calibri. Calibri does NOT have to be used but just want to level set the size.
* Use Birchline Supply colors (red, black, and white).
* Graphics and design must be super amazing to look at
* The document Word titled "Item Change Management" has most of the content needed. Use the provided photos as you see fit.
* Important: I would like the Excel file to appear in the 2-page brochure. The Word document titled Item Change Management Sales Floor and Back Office Actions is the legend for the Excel file (rows 8,9,16, and 17 of Excel file).

Target Market(s)

Birchline Supply store owners and operators

Industry/Entity Type

Retail

Font styles to use
Sans Serif

Colors
EB3D1F
EC4F4E
F09395
F8D3D4
FCEDEE

Requirements
Must have
• * Unique and look extremely creative, 8-1/2x11", font size that is readable to average eye, Birchline Supply colors, all content provided (images provided are optional), infographics where possible, the chart must look incredible.
Should not have
• Boring, too standard, traditional.

```html
<!DOCTYPE html>
<html lang="en">
<head>
<meta charset="utf-8">
<title>Item Change Management – Birchline Supply</title>
<link rel="stylesheet" href="https://fonts.googleapis.com/css2?family=Montserrat:wght@500;700;800;900&family=Open+Sans:wght@400;600;700&display=swap">
<style>
:root{
  --red:#E5202A;
  --red-soft:#EC4F4E;
  --pink:#F09395;
  --blush:#F8D3D4;
  --mist:#FCEDEE;
  --black:#141414;
  --ink:#2b2b2b;
  --white:#fff;
  --backdrop:#d9d9db;
}
*{box-sizing:border-box;margin:0;padding:0}
html,body{width:1200px;height:3520px;overflow:hidden;background:var(--backdrop)}
body{font-family:"Open Sans",Arial,sans-serif;color:var(--ink)}
.page{position:absolute;left:50px;width:1100px;height:1425px;background:var(--white);overflow:hidden;box-shadow:0 6px 24px rgba(0,0,0,.18)}
.page--front{top:60px}
.page--back{top:1605px}

/* header */
.masthead{position:relative;height:145px}
.brand{position:absolute;left:70px;top:52px;display:flex;align-items:center;gap:12px}
.brand__mark{width:26px;height:26px;background:var(--red);border-radius:50%}
.brand__name{font-family:"Montserrat",sans-serif;font-weight:800;font-size:21px;color:var(--red);line-height:1}
.brand__unit{font-family:"Montserrat",sans-serif;font-weight:700;font-size:13px;color:var(--black);letter-spacing:.5px;line-height:1.1}
.brand__unit b{display:block;color:var(--red);font-size:20px;font-weight:800;letter-spacing:0}
.hero-photo{position:absolute;left:420px;top:0;right:0;height:145px;clip-path:polygon(14% 0,100% 0,100% 100%,0 100%);background:linear-gradient(100deg,#b9c2c9 0%,#7f2a2c 30%,#e2a93a 48%,#2d5a2a 62%,#9c8a32 80%,#3a5c2c 100%)}
.title-band{height:100px;background:var(--black);position:relative;display:flex;align-items:center;padding-left:75px}
.title-band::after{content:"";position:absolute;right:0;top:0;width:40px;height:100%;background:var(--red);clip-path:polygon(60% 0,100% 0,100% 100%,0 100%)}
.title-band h1{font-family:"Montserrat",sans-serif;font-weight:900;font-size:30px;color:var(--white);letter-spacing:.2px}
.title-band h1 span{color:var(--red)}

/* faq */
.faq{display:grid;grid-template-columns:1fr 1fr;column-gap:48px;padding:28px 70px 0 70px}
.faq__col{display:flex;flex-direction:column;gap:18px}
.qa{display:grid;grid-template-columns:52px 1fr;column-gap:10px}
.qa__num{width:44px;height:44px;border-radius:50%;background:var(--black);color:var(--white);font-family:"Montserrat",sans-serif;font-weight:800;font-size:18px;display:flex;align-items:center;justify-content:center;box-shadow:0 0 0 3px var(--white),0 0 0 5px var(--red)}
.qa h3{font-family:"Montserrat",sans-serif;font-weight:700;font-size:15px;color:var(--red);line-height:1.25;text-transform:uppercase;margin-bottom:6px}
.qa p{font-size:11.6px;line-height:1.5;text-align:justify}

.checklist-wrap{padding:22px 70px 0 70px}
.checklist{border:3px solid var(--red);border-radius:14px;display:grid;grid-template-columns:repeat(5,1fr);padding:6px 0;margin-top:14px}
.checklist ul{list-style:none;border-right:1px solid var(--blush)}
.checklist ul:last-child{border-right:0}
.checklist li{display:flex;align-items:center;gap:7px;font-size:13px;font-family:"Montserrat",sans-serif;font-weight:500;padding:5px 14px;border-bottom:1px solid var(--mist)}
.checklist li svg{flex:none}

/* footer */
.footer{position:absolute;left:0;right:0;bottom:0;height:100px;display:flex;align-items:center}
.footer__phone{position:absolute;left:0;top:0;bottom:0;width:400px;background:var(--red);clip-path:polygon(0 0,100% 0,90% 100%,0 100%);display:flex;align-items:center;padding-left:70px;gap:10px;color:var(--white);font-family:"Montserrat",sans-serif;font-weight:800;font-size:28px}
.footer::after{content:"";position:absolute;left:0;right:0;bottom:0;height:12px;background:var(--red)}
.footer__links{position:absolute;left:400px;right:70px;top:0;bottom:12px;display:flex;align-items:center;justify-content:flex-end;gap:22px;font-size:17px;color:var(--black)}
.footer__links span{display:flex;align-items:center;gap:8px}

/* back page */
.masthead--back .title-block{position:absolute;left:400px;right:0;top:0;height:160px;background:var(--black);clip-path:polygon(0 0,100% 0,100% 100%,3% 100%);display:flex;align-items:center;padding-left:50px}
.masthead--back .title-block::before{content:"";position:absolute;left:0;top:0;width:30px;height:100%;background:var(--red);clip-path:polygon(0 0,100% 0,100% 100%,22% 100%)}
.title-block h1{font-family:"Montserrat",sans-serif;font-weight:900;font-size:31px;line-height:1.15;color:var(--white)}
.masthead--back{height:170px}

.legend-label{display:inline-block;margin:14px 0 0 70px;background:var(--red);color:var(--white);font-family:"Montserrat",sans-serif;font-weight:800;font-size:22px;padding:5px 40px 5px 12px;clip-path:polygon(0 0,100% 0,94% 100%,0 100%);position:relative}
.legend{display:grid;grid-template-columns:1fr 1fr;column-gap:40px;padding:14px 70px 0 80px}
.legend ol{list-style:none;display:flex;flex-direction:column;gap:12px}
.legend li{display:grid;grid-template-columns:30px 1fr;align-items:start;gap:12px;font-size:13.5px;line-height:1.35}
.dot{width:22px;height:22px;border-radius:50%;background:var(--black);color:var(--white);font-family:"Montserrat",sans-serif;font-weight:700;font-size:12px;display:flex;align-items:center;justify-content:center;box-shadow:0 0 0 2px var(--white),0 0 0 3.5px var(--black)}

.process-title{margin:22px auto 12px;width:520px;height:38px;background:var(--red);clip-path:polygon(4% 0,100% 0,96% 100%,0 100%);color:var(--white);font-family:"Montserrat",sans-serif;font-weight:800;font-size:22px;text-align:center;line-height:38px}

.matrix{width:960px;margin:0 auto;border-collapse:collapse;table-layout:fixed;font-size:9.5px;line-height:1.25;text-align:center}
.matrix th,.matrix td{border:1px solid #cfcfcf;padding:4px 3px;vertical-align:middle}
.matrix thead th{color:var(--white);font-weight:600;font-size:9.5px}
.matrix .scen{background:var(--black);font-family:"Montserrat",sans-serif;font-weight:700}
.matrix .scen-r{background:var(--red)}
.matrix .grp-red{background:var(--red)}
.matrix .grp-black{background:var(--black)}
.matrix td.row-h{text-align:left;font-weight:600;background:var(--mist)}
.matrix tbody tr:nth-child(even) td{background:#fafafa}
.matrix tbody tr:nth-child(even) td.row-h{background:var(--mist)}
.matrix + .matrix{margin-top:12px}

.asterisk{width:960px;margin:12px auto 0;background:var(--black);border-radius:8px;display:flex;align-items:center;height:54px;overflow:hidden}
.asterisk__label{background:var(--white);border:3px solid var(--red);border-radius:8px;height:100%;padding:0 26px;display:flex;align-items:center;font-family:"Montserrat",sans-serif;font-weight:800;font-size:18px;color:var(--red)}
.asterisk__text{color:var(--white);font-size:12.5px;padding-left:26px;line-height:1.45}
</style>
</head>
<body>

<!-- FRONT -->
<section class="page page--front">
  <header class="masthead">
    <div class="brand">
      <span class="brand__mark"></span>
      <span class="brand__name">Birchline<br>Supply</span>
      <span class="brand__unit">STORE SYSTEMS &amp;<b>OPERATIONS</b></span>
    </div>
    <div class="hero-photo" role="img" aria-label="Store associate in a red vest scanning insect repellent cans on a shelf"></div>
  </header>
  <div class="title-band"><h1><span>ITEM CHANGE MANAGEMENT</span> FREQUENTLY ASKED QUESTIONS:</h1></div>

  <div class="faq">
    <div class="faq__col">
      <article class="qa"><div class="qa__num">01</div><div><h3>Why do I even need to do Item Change Management (ICM)?</h3><p>ICM simplifies and reduces the amount time and effort to manage the process of identifying and taking action against canceled, replacement, and reinstated items. Without ICM, the process of doing so is manual and laborious, error prone, and ultimately can result in taking lost sales. Contrarily, leveraging ICM (versus other manual approaches) typically saves stores between 8-12 hours per month, increase inventory accurateness, and improved operational effectiveness on the sales floor.</p></div></article>
      <article class="qa"><div class="qa__num">02</div><div><h3>How frequently should I be working ICM?</h3><p>Weekly. This keeps the execution manageable and steady. Aim for consistency by performing ICM the same day each week.</p></div></article>
      <article class="qa"><div class="qa__num">03</div><div><h3>My computer is ordering the replacement SKU when I'm not out of stock on the discontinued product. Why?</h3><p>Confirm option configuration setting 9972 is set to option '2'. Doing so tells the system to order the new product only when the discontinued item falls to zero on hand.</p></div></article>
      <article class="qa"><div class="qa__num">04</div><div><h3>I heard ICM merges product information. I've been using RCIN in Kestrel for years to do that. Do I still need to use RCIN?</h3><p>Managing items via ICM renders the need to do RCIN obsolete. ICM doesn't technically 'merge' items because doing so creates inventory issues as well as a loss of visibility to discontinued SKUs. ICM, on the other hand, copies over certain key information from the discontinued item to the new item, keeping the discontinued item intact to retain visibility and minimize long-term inventory accuracy issues.</p></div></article>
      <article class="qa"><div class="qa__num">05</div><div><h3>I'm in on ICM. How do I get started?</h3><p>Great! Start by reviewing the Birchline Way of Retailing Practice titled Item Change Management (Cancelled, Replacement, Temporary Closeout, and Reinstated Items) – Setup. Path: BIRCHNET &gt; About Birchline – Birchline Way of Retailing &gt; BWOR Search: ICM.</p></div></article>
    </div>
    <div class="faq__col">
      <article class="qa"><div class="qa__num">06</div><div><h3>What in the world is the RICR report, and how does it relate to ICM?</h3><p>RICR stands for 'Item Change Report' and prints after finalizing your work in ICM. Review it in the back office and on the sales floor as a means to update location codes and bin labels.</p></div></article>
      <article class="qa"><div class="qa__num">07</div><div><h3>Does ICM have any effect on my in-stock percentage measurement?</h3><p>Undoubtably. Stores regularly leveraging ICM weekly have shown to have a higher in-stock percentage than those that don't. ICM allows retailers to react faster and more effectively to items going away ensuring an effective plan is in place. Also, taking action against temporary out of stocks using ICM doesn't negatively impact your in-stock percentage.</p></div></article>
      <article class="qa"><div class="qa__num">08</div><div><h3>If I don't stock the SKU, will it appear in ICM?</h3><p>No. Your ICM list is store specific, not a report of everything carried in the RSC. In other words, items you have not sold or purchased from the RSC in the last three years do not appear in the program for you to action.</p></div></article>
      <article class="qa"><div class="qa__num">09</div><div><h3>I have five stores in my chain. Can I review and execute ICM for all of them in one fell swoop?</h3><p>Sure. The reporting in ICM can be reviewed and executed centrally creating greater efficiencies when executing. Upon entering the BIRCHNET application, simply click the multi-store icon to select the stores you want to work on.</p></div></article>
      <article class="qa"><div class="qa__num">10</div><div><h3>I don't know if my SKUs are updating properly – how do I confirm?</h3><p>Compare the BIRCHNET PDF (available upon finalizing your work) to the Kestrel RICR report to ensure all information has transmitted properly. If need be, you can also run the RICR report manually to serve as an audit tool. Within the ICM application, there is also an option to review previously finalized items for further investigation.</p></div></article>
      <article class="qa"><div class="qa__num">11</div><div><h3>Who do I contact with any further questions and support?</h3><p>Your field representative is always available to help answer questions. For further details about the program, you can also contact the Store Systems and Operations team.</p></div></article>
    </div>
  </div>

  <div class="checklist-wrap">
    <article class="qa"><div class="qa__num">12</div><div><h3 style="margin-top:12px">I'm in on ICM. How do I get started?</h3></div></article>
    <div class="checklist">
      <ul><li><svg width="12" height="12" viewBox="0 0 12 12"><circle cx="6" cy="6" r="5" fill="none" stroke="#E5202A" stroke-width="1.3"/><path d="M3.5 6.2l1.7 1.6 3.3-3.4" fill="none" stroke="#E5202A" stroke-width="1.3"/></svg>DATE ADDED</li><li><svg width="12" height="12" viewBox="0 0 12 12"><circle cx="6" cy="6" r="5" fill="none" stroke="#E5202A" stroke-width="1.3"/><path d="M3.5 6.2l1.7 1.6 3.3-3.4" fill="none" stroke="#E5202A" stroke-width="1.3"/></svg>ROP PROTECT</li><li><svg width="12" height="12" viewBox="0 0 12 12"><circle cx="6" cy="6" r="5" fill="none" stroke="#E5202A" stroke-width="1.3"/><path d="M3.5 6.2l1.7 1.6 3.3-3.4" fill="none" stroke="#E5202A" stroke-width="1.3"/></svg>ORDER POINT</li><li><svg width="12" height="12" viewBox="0 0 12 12"><circle cx="6" cy="6" r="5" fill="none" stroke="#E5202A" stroke-width="1.3"/><path d="M3.5 6.2l1.7 1.6 3.3-3.4" fill="none" stroke="#E5202A" stroke-width="1.3"/></svg>LOCATION CODE(S)</li><li><svg width="12" height="12" viewBox="0 0 12 12"><circle cx="6" cy="6" r="5" fill="none" stroke="#E5202A" stroke-width="1.3"/><path d="M3.5 6.2l1.7 1.6 3.3-3.4" fill="none" stroke="#E5202A" stroke-width="1.3"/></svg>EXPANDED PROMO HISTORY</li></ul>
      <ul><li><svg width="12" height="12" viewBox="0 0 12 12"><circle cx="6" cy="6" r="5" fill="none" stroke="#E5202A" stroke-width="1.3"/><path d="M3.5 6.2l1.7 1.6 3.3-3.4" fill="none" stroke="#E5202A" stroke-width="1.3"/></svg>Sales History</li><li><svg width="12" height="12" viewBox="0 0 12 12"><circle cx="6" cy="6" r="5" fill="none" stroke="#E5202A" stroke-width="1.3"/><path d="M3.5 6.2l1.7 1.6 3.3-3.4" fill="none" stroke="#E5202A" stroke-width="1.3"/></svg>Max Stock Level</li><li><svg width="12" height="12" viewBox="0 0 12 12"><circle cx="6" cy="6" r="5" fill="none" stroke="#E5202A" stroke-width="1.3"/><path d="M3.5 6.2l1.7 1.6 3.3-3.4" fill="none" stroke="#E5202A" stroke-width="1.3"/></svg>Special Fees</li><li><svg width="12" height="12" viewBox="0 0 12 12"><circle cx="6" cy="6" r="5" fill="none" stroke="#E5202A" stroke-width="1.3"/><path d="M3.5 6.2l1.7 1.6 3.3-3.4" fill="none" stroke="#E5202A" stroke-width="1.3"/></svg>Signature Required</li><li><svg width="12" height="12" viewBox="0 0 12 12"><circle cx="6" cy="6" r="5" fill="none" stroke="#E5202A" stroke-width="1.3"/><path d="M3.5 6.2l1.7 1.6 3.3-3.4" fill="none" stroke="#E5202A" stroke-width="1.3"/></svg>Popularity Code</li></ul>
      <ul><li><svg width="12" height="12" viewBox="0 0 12 12"><circle cx="6" cy="6" r="5" fill="none" stroke="#E5202A" stroke-width="1.3"/><path d="M3.5 6.2l1.7 1.6 3.3-3.4" fill="none" stroke="#E5202A" stroke-width="1.3"/></svg>PO Season Code</li><li><svg width="12" height="12" viewBox="0 0 12 12"><circle cx="6" cy="6" r="5" fill="none" stroke="#E5202A" stroke-width="1.3"/><path d="M3.5 6.2l1.7 1.6 3.3-3.4" fill="none" stroke="#E5202A" stroke-width="1.3"/></svg>Tax Status</li><li><svg width="12" height="12" viewBox="0 0 12 12"><circle cx="6" cy="6" r="5" fill="none" stroke="#E5202A" stroke-width="1.3"/><path d="M3.5 6.2l1.7 1.6 3.3-3.4" fill="none" stroke="#E5202A" stroke-width="1.3"/></svg># of Labels</li><li><svg width="12" height="12" viewBox="0 0 12 12"><circle cx="6" cy="6" r="5" fill="none" stroke="#E5202A" stroke-width="1.3"/><path d="M3.5 6.2l1.7 1.6 3.3-3.4" fill="none" stroke="#E5202A" stroke-width="1.3"/></svg>Expanded Sales History</li></ul>
      <ul><li><svg width="12" height="12" viewBox="0 0 12 12"><circle cx="6" cy="6" r="5" fill="none" stroke="#E5202A" stroke-width="1.3"/><path d="M3.5 6.2l1.7 1.6 3.3-3.4" fill="none" stroke="#E5202A" stroke-width="1.3"/></svg>Tally</li><li><svg width="12" height="12" viewBox="0 0 12 12"><circle cx="6" cy="6" r="5" fill="none" stroke="#E5202A" stroke-width="1.3"/><path d="M3.5 6.2l1.7 1.6 3.3-3.4" fill="none" stroke="#E5202A" stroke-width="1.3"/></svg>Loading Required</li><li><svg width="12" height="12" viewBox="0 0 12 12"><circle cx="6" cy="6" r="5" fill="none" stroke="#E5202A" stroke-width="1.3"/><path d="M3.5 6.2l1.7 1.6 3.3-3.4" fill="none" stroke="#E5202A" stroke-width="1.3"/></svg>Birchline MSU's</li><li><svg width="12" height="12" viewBox="0 0 12 12"><circle cx="6" cy="6" r="5" fill="none" stroke="#E5202A" stroke-width="1.3"/><path d="M3.5 6.2l1.7 1.6 3.3-3.4" fill="none" stroke="#E5202A" stroke-width="1.3"/></svg>CPP Discounts</li></ul>
      <ul><li><svg width="12" height="12" viewBox="0 0 12 12"><circle cx="6" cy="6" r="5" fill="none" stroke="#E5202A" stroke-width="1.3"/><path d="M3.5 6.2l1.7 1.6 3.3-3.4" fill="none" stroke="#E5202A" stroke-width="1.3"/></svg>Discountable</li><li><svg width="12" height="12" viewBox="0 0 12 12"><circle cx="6" cy="6" r="5" fill="none" stroke="#E5202A" stroke-width="1.3"/><path d="M3.5 6.2l1.7 1.6 3.3-3.4" fill="none" stroke="#E5202A" stroke-width="1.3"/></svg>User codes</li><li><svg width="12" height="12" viewBox="0 0 12 12"><circle cx="6" cy="6" r="5" fill="none" stroke="#E5202A" stroke-width="1.3"/><path d="M3.5 6.2l1.7 1.6 3.3-3.4" fill="none" stroke="#E5202A" stroke-width="1.3"/></svg>Promo History</li><li><svg width="12" height="12" viewBox="0 0 12 12"><circle cx="6" cy="6" r="5" fill="none" stroke="#E5202A" stroke-width="1.3"/><path d="M3.5 6.2l1.7 1.6 3.3-3.4" fill="none" stroke="#E5202A" stroke-width="1.3"/></svg>Sells with SKU</li></ul>
    </div>
  </div>

  <footer class="footer">
    <div class="footer__phone"><svg width="30" height="30" viewBox="0 0 30 30"><circle cx="15" cy="15" r="14" fill="#fff"/><path d="M10 8l3 0 1.5 4-2 1.3a9 9 0 0 0 4.2 4.2L18 15.5l4 1.5v3c0 1-1 2-2 2A12 12 0 0 1 8 10c0-1 1-2 2-2z" fill="#E5202A"/></svg>555.014.2290</div>
    <div class="footer__links">
      <span><svg width="26" height="26" viewBox="0 0 26 26"><circle cx="13" cy="13" r="12" fill="#141414"/><rect x="7" y="9" width="12" height="8" rx="1" fill="none" stroke="#fff" stroke-width="1.4"/><path d="M7 9l6 5 6-5" fill="none" stroke="#fff" stroke-width="1.4"/></svg>storeops@birchlinesupply.com</span>
      <span><svg width="26" height="26" viewBox="0 0 26 26"><circle cx="13" cy="13" r="12" fill="#141414"/><circle cx="13" cy="13" r="6.5" fill="none" stroke="#fff" stroke-width="1.3"/><path d="M6.5 13h13M13 6.5c-3 3.5-3 9.5 0 13M13 6.5c3 3.5 3 9.5 0 13" fill="none" stroke="#fff" stroke-width="1.2"/></svg>www.birchlinesupply.com</span>
    </div>
  </footer>
</section>

<!-- BACK -->
<section class="page page--back">
  <header class="masthead masthead--back">
    <div class="brand">
      <span class="brand__mark"></span>
      <span class="brand__name">Birchline<br>Supply</span>
      <span class="brand__unit">STORE SYSTEMS &amp;<b>OPERATIONS</b></span>
    </div>
    <div class="title-block"><h1>ITEM CHANGE MANAGEMENT:&nbsp; SALES<br>FLOOR AND BACK OFFICE ACTIONS</h1></div>
  </header>

  <div class="legend-label">SALES FLOOR ACTIONS LEGEND:</div>
  <div class="legend">
    <ol>
      <li><span class="dot">A</span>Mark bin label with red dot</li>
      <li><span class="dot">B</span>Write replacement SKU number inside red dot</li>
      <li><span class="dot">C</span>Affix temporary closeout signage to shelf space of discontinued item. Complete this action when quantity on hand of the temporary closeout item falls to zero</li>
      <li><span class="dot">D</span>Write currently stocked replacement SKU number and its location on the temporary closeout signage</li>
      <li><span class="dot">E</span>Remove bin label from discontinued SKU when quantity on hand falls to zero</li>
      <li><span class="dot">F</span>Swap out bin label from discontinued SKU with new bin label when merchandising new item</li>
    </ol>
    <ol>
      <li><span class="dot">G</span>Remove temp closeout Birchline recommended signage from shelf space upon it becoming reinstated</li>
      <li><span class="dot">H</span>Merchandise new replacements in same location as the temporary or permanent discontinued item's location, if you don't currently stock replacement</li>
      <li><span class="dot">I</span>Leave bin label intact and preserve space for when the item is reinstated</li>
      <li><span class="dot">J</span>Create a new space for reinstated item and new bin label, when applicable</li>
      <li><span class="dot">K</span>Merchandise temporary closeout items in their original location upon being reinstated</li>
    </ol>
  </div>

  <div class="legend-label">BACK OFFICE ACTIONS LEGEND:</div>
  <div class="legend">
    <ol>
      <li><span class="dot">A</span>Change the location code of discontinued item to CLOSE when items sells out</li>
      <li><span class="dot">B</span>Update location and/or minimum order point for replacement when applicable</li>
    </ol>
    <ol>
      <li><span class="dot">C</span>Change store closeout flag to 'Y' for reinstated SKU, if not already completed</li>
      <li><span class="dot">D</span>Manually update in Kestrel to new vendor</li>
    </ol>
  </div>

  <div class="process-title">ITEM CHANGE MANAGEMENT PROCESS</div>

  <table class="matrix">
    <colgroup><col style="width:82px"><col span="10"><col style="width:82px"></colgroup>
    <thead>
      <tr><th class="scen">SCENARIO</th><th class="grp-red" colspan="2">Birchline Discontinues an Item with No Replacement</th><th class="grp-black" colspan="2">Birchline Temporarily Closes an Item Out with No Recommended Replacement</th><th class="grp-red" colspan="3">Birchline Discontinues Item with Direct or Suggested Replacement</th><th class="grp-black" colspan="3">Birchline Temporarily Closes an Item Out with Direct or Suggested Replacement</th><th class="scen scen-r">Scenario</th></tr>
    </thead>
    <tbody>
      <tr><td class="row-h">Will You Stock Replacement?</td><td>N/A</td><td>Find an Alternate Vendor</td><td>N/A</td><td>Find an Alternate Vendor</td><td>Yes</td><td>No* Closeout</td><td>Find an Alternate Vendor</td><td>Yes</td><td>No** Temp Closeout</td><td>Find an Alternate Vendor</td><td class="row-h">Will You Stock Replacement?</td></tr>
      <tr><td class="row-h">ICM Action:</td><td>Closeout Discontinued Item</td><td>Remove from List</td><td>Temp Closeout</td><td>Remove from List</td><td>Closeout &amp; Accept Repl</td><td>Closeout &amp; Discontinued Item*</td><td>Remove from List</td><td>Temporary Closeout &amp; Accept Replacement</td><td>Store Closeout Flag is Set to 'D'</td><td>Remove from List</td><td class="row-h">ICM Action</td></tr>
      <tr><td class="row-h">What Happens in Kestrel?</td><td>Store Closeout Flag is Set to 'B'</td><td>Remove from List</td><td>Store Closeout Flag is Set to 'B'</td><td>N/A</td><td>Store Closeout Flag is Set to 'B'</td><td>N/A</td><td>Store Closeout Flag is Set to 'T'</td><td>Store Closeout Flag is Set to 'T'; Keep temp closeout off the RSC</td><td>C, D*, G, I</td><td>N/A</td><td class="row-h">What Happens in Kestrel?</td></tr>
      <tr><td class="row-h">Sales Floor Actions:</td><td>A, E, L</td><td>A, B, F, H, L</td><td>C, G, I</td><td>C, D, F, G, H</td><td>A, B, F, H, L</td><td>A, E, L</td><td>A, B, F, H, L</td><td>C, D, F, G, H</td><td></td><td>C, D, F, G, H</td><td class="row-h">Sales Floor Actions:</td></tr>
      <tr><td class="row-h">Back Office Actions:</td><td></td><td>A, B, F, H, L</td><td></td><td>M, O</td><td>M</td><td>M, O</td><td></td><td>M</td><td></td><td>M, O</td><td class="row-h">Back Office Actions:</td></tr>
    </tbody>
  </table>

  <table class="matrix">
    <colgroup><col style="width:82px"><col span="7"><col style="width:82px"></colgroup>
    <thead>
      <tr><th class="scen">SCENARIO</th><th class="grp-red" colspan="3">Birchline Reinstates Item with No Previous Associated Replacement SKU</th><th class="grp-black" colspan="4">Birchline Reinstates Items with Previously Associated Replacement SKU</th><th class="scen scen-r">Scenario</th></tr>
    </thead>
    <tbody>
      <tr><td class="row-h">Will You Stock the Reinstated Item Again?</td><td>Yes</td><td>No</td><td>No Decision (Not Recommended)</td><td>Yes</td><td>Yes</td><td>No</td><td>No</td><td class="row-h">Will You Stock the Reinstated Item Again?</td></tr>
      <tr><td class="row-h">Keep Replacement?</td><td>N/A</td><td>N/A</td><td>N/A</td><td>No</td><td>Yes</td><td>No</td><td>Yes</td><td class="row-h">Keep Replacement?</td></tr>
      <tr><td class="row-h">ICM Action:</td><td>Reinstate Item</td><td>Remove from List?</td><td>N/A</td><td>Activate Original SKU &amp; Closeout Replacement</td><td>Activate Original SKU &amp; Keep Replacement</td><td>Closeout Original SKU &amp; Closeout Replacement</td><td>Closeout Original SKU &amp; Keep Replacement</td><td class="row-h">ICM Action:</td></tr>
      <tr><td class="row-h">What Happens in Kestrel?</td><td>Store Closeout flag = N on original temp closeout SKU</td><td>Store Closeout flag = Y on original temp closeout SKU</td><td>No Change – If Store Closeout field is Not Changed</td><td>** Store Closeout flag = N on original temp closeout SKU</td><td>** Store Closeout flag = N on original temp closeout SKU</td><td>** Store Closeout flag remains as 'Y' on original SKU</td><td>** Store Closeout flag remains as 'N' on replacement</td><td class="row-h">What Happens in Kestrel?</td></tr>
      <tr><td class="row-h">Sales Floor Actions:</td><td>J or K</td><td>E**, G**</td><td>Approach not recommended</td><td>A, B, E, K</td><td>I</td><td>A, E</td><td>I</td><td class="row-h">Sales Floor Actions:</td></tr>
      <tr><td class="row-h">Back Office Actions:</td><td>M</td><td>L**, M**</td><td>Approach not recommended</td><td>L, M</td><td>M</td><td>L**, M**</td><td>N**</td><td class="row-h">Back Office Actions:</td></tr>
    </tbody>
  </table>

  <div class="asterisk">
    <div class="asterisk__label">ASTERISK ITEMS:</div>
    <div class="asterisk__text">* Could apply this action if you already stock the replacement and do not want to combine sales history<br>** Take action only when applicable</div>
  </div>

  <footer class="footer">
    <div class="footer__phone"><svg width="30" height="30" viewBox="0 0 30 30"><circle cx="15" cy="15" r="14" fill="#fff"/><path d="M10 8l3 0 1.5 4-2 1.3a9 9 0 0 0 4.2 4.2L18 15.5l4 1.5v3c0 1-1 2-2 2A12 12 0 0 1 8 10c0-1 1-2 2-2z" fill="#E5202A"/></svg>555.014.2290</div>
    <div class="footer__links">
      <span><svg width="26" height="26" viewBox="0 0 26 26"><circle cx="13" cy="13" r="12" fill="#141414"/><rect x="7" y="9" width="12" height="8" rx="1" fill="none" stroke="#fff" stroke-width="1.4"/><path d="M7 9l6 5 6-5" fill="none" stroke="#fff" stroke-width="1.4"/></svg>storeops@birchlinesupply.com</span>
      <span><svg width="26" height="26" viewBox="0 0 26 26"><circle cx="13" cy="13" r="12" fill="#141414"/><circle cx="13" cy="13" r="6.5" fill="none" stroke="#fff" stroke-width="1.3"/><path d="M6.5 13h13M13 6.5c-3 3.5-3 9.5 0 13M13 6.5c3 3.5 3 9.5 0 13" fill="none" stroke="#fff" stroke-width="1.2"/></svg>www.birchlinesupply.com</span>
    </div>
  </footer>
</section>

</body>
</html>
```